Tallow Creek Stampede Sponsor Brochure/letter

We are wanting a professional looking brochure/letter that can be given to potential sponsors. This can be multiple pages the last page needs to be the Invoice (attached example) the prices on the example can be used.. this is a first nation rodeo and we are looking for sponsorship I can provide more photos if needed

Target Market(s)

This will be local corporate business's so this needs to be very professional looking

Industry/Entity Type

This is an event but we are looking for cooperate sponsorship

Font styles to use
Serif

Colors
0054AA
0677BA
7BADD7
CADEEF
E8F1F8
FFC000
F8CF3A
FAE287
FDF2CF
FEFAEE
F0912C
F2A743
F7CA91
FBE8D2
FDF5EE
EB3D1F
EC4F4E
F09395
F8D3D4
FCEDEE

Requirements
Must have
• The basic information, must have some quotes and photos can be multiple pages
Nice to have
• I would like to see that it is interactive, but gets to the point
Should not have
• no cartoon or must not look cheap

```html
<!DOCTYPE html>
<html lang="en">
<head>
<meta charset="utf-8">
<title>Tallow Creek Stampede – Sponsorship Proposal</title>
<link rel="stylesheet" href="https://fonts.googleapis.com/css2?family=Bebas+Neue&family=Oswald:wght@400;500;600&family=Open+Sans:wght@400;600;700&family=Montserrat:wght@500;700;800&display=swap">
<style>
:root{
  --canvas:#a9b4cd;
  --navy:#0e1f52;
  --blue:#29a9e1;
  --orange:#f6a81f;
  --paper:#ffffff;
  --ink:#222631;
  --grey-cell:#eeeeee;
  --grey-cell-alt:#e6e6e6;
  --grey-bar:#dcdcdc;
  --green:#7ac143;
  --bronze:#5b3a1c;
  --silver:#b7b7b7;
  --platinum:#6d6e71;
  --saloon:#79c043;
  --pancake:#2e9a46;
  --kids:#e0262e;
}
*{box-sizing:border-box;margin:0;padding:0}
html,body{width:1200px;height:2338px;overflow:hidden}
body{background:var(--canvas);font-family:"Open Sans",sans-serif;color:var(--ink);position:relative}
.page{position:absolute;background:var(--paper);overflow:hidden;box-shadow:0 1px 4px rgba(0,0,0,.18)}
.abs{position:absolute}
.photo{position:absolute}

/* brand placeholder */
.brand{position:absolute;display:flex;align-items:center;gap:10px}
.brand-dot{width:34px;height:34px;border-radius:50%;background:var(--blue);flex:none}
.brand-name{font-family:"Oswald",sans-serif;font-weight:500;color:var(--navy);text-transform:uppercase;line-height:1.1}

/* page 1 – proposal */
.proposal{left:58px;top:106px;width:522px;height:678px}
.proposal .brand{left:52px;top:28px}
.proposal .brand-name{font-size:22px;width:170px}
.proposal .hero-photo{left:286px;top:0;width:236px;height:284px;background:linear-gradient(160deg,#c9c2b3 0%,#8d806a 45%,#5a4733 75%,#3e4b5e 100%);clip-path:polygon(10% 0,100% 0,100% 100%,0 100%)}
.title-panel{left:0;top:110px;width:318px;height:174px;background:var(--navy);clip-path:polygon(0 0,100% 0,92% 100%,0 100%)}
.title-main{position:absolute;left:14px;top:116px;width:300px;font-family:"Bebas Neue",sans-serif;font-size:45px;color:#fff;text-align:center;letter-spacing:.5px}
.title-sub{position:absolute;left:14px;top:168px;width:300px;display:flex;align-items:center;gap:12px;font-family:"Oswald",sans-serif;font-size:22px;letter-spacing:4px;color:var(--blue);text-transform:uppercase}
.title-sub::before,.title-sub::after{content:"";flex:1;height:1.5px;background:#fff}
.quote-box{position:absolute;left:14px;top:204px;width:284px;height:70px;border:1.5px solid #fff;font-family:"Oswald",sans-serif;font-weight:500;font-size:13.5px;line-height:1.3;color:#fff;text-align:center;padding-top:8px}
.quote-box cite{display:block;font-style:normal;color:var(--blue)}
.lead-band{left:0;top:284px;width:522px;height:63px;background:var(--blue);color:#fff;font-family:"Oswald",sans-serif;font-weight:500;font-size:14.5px;text-transform:uppercase;text-align:center;line-height:1.3;padding-top:12px}
.letter-body{left:16px;top:358px;width:490px;font-size:9.3px;line-height:1.33;text-align:justify}
.letter-body p{margin-bottom:9px}
.proposal-footer{left:0;top:606px;width:522px;height:72px}
.footer-contact{position:absolute;left:0;top:0;width:322px;height:72px;background:var(--navy);clip-path:polygon(0 0,96% 0,100% 100%,0 100%);color:#fff;font-size:9.5px;font-weight:600;padding:18px 0 0 16px;line-height:1.55}
.footer-contact .hl{color:var(--blue)}
.footer-contact .row{display:flex;align-items:center;gap:5px}
.footer-contact svg{width:10px;height:10px;flex:none}
.footer-web{position:absolute;right:0;top:34px;width:220px;height:38px;background:var(--blue);color:#fff;font-family:"Oswald",sans-serif;font-weight:500;font-size:14px;letter-spacing:.5px;text-align:center;line-height:38px}
.footer-web::before{content:"";position:absolute;left:-14px;top:-34px;width:18px;height:72px;background:var(--blue);transform:skewX(10deg)}

/* page 2 – dates */
.dates{left:618px;top:106px;width:522px;height:678px}
.dates .action-photo{left:0;top:0;width:300px;height:282px;background:linear-gradient(170deg,#8c9c74 0%,#6e7d55 35%,#7d6648 60%,#a58f72 100%)}
.date-panel{left:272px;top:0;width:250px;height:282px;background:var(--orange);clip-path:polygon(6% 0,100% 0,100% 100%,0 100%)}
.date-head{position:absolute;left:290px;top:14px;width:232px;text-align:center;font-family:"Bebas Neue",sans-serif;font-size:44px;color:#fff;letter-spacing:.5px}
.day-box{position:absolute;width:66px;height:66px;background:var(--navy);color:#fff;font-family:"Bebas Neue",sans-serif;font-size:54px;line-height:70px;text-align:center;outline:2px solid #fff;outline-offset:-5px}
.date-month{position:absolute;left:290px;top:222px;width:232px;text-align:center;font-family:"Bebas Neue",sans-serif;font-size:46px;color:#fff}
.intro-band{left:0;top:282px;width:522px;height:65px;background:var(--blue);color:#fff;font-size:9.2px;font-weight:600;line-height:1.3;padding:12px 22px 0 24px}
.sched-day{position:absolute;left:22px;width:42px;height:43px;background:var(--navy);color:#fff;font-family:"Bebas Neue",sans-serif;font-size:32px;line-height:46px;text-align:center}
.sched-note{position:absolute;left:103px;font-size:9px;line-height:1.5;color:#333}
.sched-rule{position:absolute;left:100px;width:404px;height:1.5px;background:#999}
.slot{position:absolute;left:95px;width:181px;height:24px;font-family:"Montserrat",sans-serif;font-weight:500;font-size:9px;color:#fff;display:flex;justify-content:space-between;align-items:center;padding:0 8px}
.slot.junior{background:var(--orange)}
.slot.main{background:var(--navy)}
.dates-footer{left:0;top:593px;width:446px;height:85px;background:var(--navy);clip-path:polygon(0 0,100% 0,95% 100%,0 100%);font-size:9.2px;color:#fff;padding:19px 0 0 24px;line-height:1.5}
.dates-footer .label{color:var(--orange)}

/* page 3 – packages */
.packages{left:58px;top:836px;width:1084px;height:702px}
.packages .brand{left:26px;top:40px}
.packages .brand-name{font-size:24px;width:180px}
.pack-banner{left:338px;top:0;width:531px;height:94px;background:var(--navy);clip-path:polygon(0 0,100% 0,97% 100%,3% 100%);color:#fff;font-family:"Bebas Neue",sans-serif;font-size:70px;text-align:center;line-height:100px;letter-spacing:1px}
.pack-table{position:absolute;left:36px;top:145px;width:999px;border-collapse:collapse;table-layout:fixed}
.pack-table col.label{width:140px}
.pack-table thead th{height:60px;font-family:"Oswald",sans-serif;font-weight:500;font-size:13px;line-height:1.15;color:#fff;text-transform:uppercase;text-align:center;vertical-align:middle}
.pack-table thead th:first-child{background:transparent}
.pack-table thead th:nth-child(2){background:var(--navy)}
.pack-table thead th:nth-child(3){background:var(--bronze)}
.pack-table thead th:nth-child(4){background:var(--silver)}
.pack-table thead th:nth-child(5){background:var(--orange)}
.pack-table thead th:nth-child(6){background:var(--platinum)}
.pack-table thead th:nth-child(7){background:var(--saloon)}
.pack-table thead th:nth-child(8){background:var(--pancake)}
.pack-table thead th:nth-child(9){background:var(--kids)}
.pack-table thead th:nth-child(10){background:var(--blue)}
.pack-table tbody th{font-family:"Open Sans",sans-serif;font-weight:600;font-size:9.8px;line-height:1.25;text-transform:uppercase;text-align:left;color:#1b1b1b;padding-left:4px;vertical-align:middle}
.pack-table tbody td{text-align:center;vertical-align:middle;background:var(--grey-cell)}
.pack-table tbody td:nth-child(odd){background:var(--grey-cell-alt)}
.pack-table tbody tr:not(:last-child) th,
.pack-table tbody tr:not(:last-child) td{border-bottom:1.5px solid #2e3c68}
.pack-table tbody td:nth-child(2){color:var(--navy)}
.pack-table tbody td:nth-child(3){color:var(--bronze)}
.pack-table tbody td:nth-child(4){color:#9a9a9a}
.pack-table tbody td:nth-child(5){color:var(--orange)}
.pack-table tbody td:nth-child(6){color:#4a4b4e}
.pack-table tbody td:nth-child(7){color:var(--saloon)}
.pack-table tbody td:nth-child(8){color:var(--pancake)}
.pack-table tbody td:nth-child(9){color:var(--kids)}
.pack-table tbody td:nth-child(10){color:var(--blue)}
.tick{width:19px;height:16px;vertical-align:middle}
.qty{font-size:12px;color:#222;margin-left:5px;vertical-align:middle}
.note{display:block;font-size:9.5px;font-weight:600;color:#222;margin-bottom:14px}
.row-radio td{vertical-align:bottom;padding-bottom:6px}

/* page 4 – invoice */
.invoice{left:319px;top:1586px;width:523px;height:672px;font-family:"Montserrat",sans-serif}
.invoice .brand{left:26px;top:72px}
.invoice .brand-name{font-size:21px;width:170px}
.inv-title{left:232px;top:0;width:271px;height:46px;background:var(--green);color:#fff;font-weight:800;font-size:32px;letter-spacing:2px;text-align:center;line-height:50px}
.inv-cust-bar{left:232px;top:48px;width:271px;height:17px;background:var(--grey-bar);font-weight:700;font-size:9px;text-align:center;line-height:17px;letter-spacing:.5px}
.inv-cust{left:237px;top:70px;font-size:7.3px;line-height:1.38}
.inv-cust b{font-weight:700;display:block;text-transform:uppercase}
.inv-cust span{display:block;font-family:"Open Sans",sans-serif;color:#555}
.sec-bar{position:absolute;left:23px;width:481px;height:13px;background:var(--blue);color:#fff;font-weight:700;font-size:9.5px;text-align:center;line-height:13px;letter-spacing:.5px}
.sec-head{position:absolute;left:23px;width:481px;height:12px;background:var(--grey-bar);font-weight:700;font-size:8px;line-height:12px}
.sec-head span{position:absolute}
.item-list{position:absolute;left:42px;font-size:8px;font-weight:500;line-height:20.5px}
.vline{position:absolute;width:1.5px;background:var(--blue)}
.sum-bar{position:absolute;width:167px;height:20px;background:var(--green)}
.total-label{left:338px;top:532px;width:166px;height:19px;background:var(--grey-bar);font-weight:700;font-size:8.5px;text-align:center;line-height:19px}
.total-box{left:338px;top:558px;width:166px;height:32px;border:1.5px solid var(--blue)}
.paid{left:42px;top:565px;font-size:7.5px;line-height:1.3}
.paid b{display:block;font-weight:700}
.inv-footer{left:0;top:622px;width:523px;height:50px;background:var(--blue);color:#fff;font-size:9px;font-weight:500}
.inv-footer span{position:absolute;top:26px}
.inv-name{left:107px;top:613px;width:299px;height:17px;background:#111;border-radius:4px;color:#fff;font-weight:700;font-size:10px;text-align:center;line-height:17px;letter-spacing:.5px}
</style>
</head>
<body>

<svg width="0" height="0" style="position:absolute" aria-hidden="true">
  <symbol id="tick" viewBox="0 0 24 20">
    <path d="M2 11.5 L8.5 18 L22 2" fill="none" stroke="currentColor" stroke-width="2.6" stroke-linecap="round" stroke-linejoin="round"/>
  </symbol>
</svg>

<!-- Page 1: proposal letter -->
<section class="page proposal">
  <div class="brand"><span class="brand-dot"></span><span class="brand-name">Tallow Creek First Nation</span></div>
  <div class="photo hero-photo" role="img" aria-label="Photo of a bronc rider on a bucking horse leaving the chute"></div>
  <div class="abs title-panel"></div>
  <h1 class="title-main">Rodeo Sponsorship</h1>
  <div class="title-sub">Proposal</div>
  <blockquote class="quote-box">“Courage is being scared to death<br>and saddling up anyway!”<cite>– Hank Carver</cite></blockquote>
  <div class="abs lead-band">2 one day rodeos with amazing prizes and buckles each day<br>with the average winning a TCFN drum!</div>
  <div class="abs letter-body">
    <p>The Tallow Creek Stampede is an attraction to many local cowboys and cowgirls from local communities, Fort St. John and across BC, AB and surrounding areas.  We offer youth to adult events that are all crowd pleasers.</p>
    <p>Since the beginning this has been an annual event up until Covid-19 when we have had to take a break but we are so excited to build it bigger and better then before!</p>
    <p>We have some big plans for the future of the Tallow Creek Stampede including an expansion of the Rodeo grounds, new event buildings, new office/announcer booths as well as the purchase of new grandstands.  This will be a big endeavor that we think will benefit both our community as well as the local community.</p>
    <p>Our rodeo would not have flourished without the support and generosity we have received from your sponsorship over the years.  Once again, we are hoping your company will give generously to our yearly event and help continue to make our rodeo a success. All support goes towards any supplies not covered by donation, the purchase of materials to upgrade the rodeo grounds, rodeo stock and event payout.  We hope to attract even more rodeo events, larger entertainers, and more fans through the gates.  Your sponsorship will be highly regarded for what we hope will be generations to come.</p>
    <p>Please see the level of sponsorship attached, fill and return to the Tallow Creek Stampede!<br>Your sponsorship is greatly appreciated.</p>
  </div>
  <footer class="abs proposal-footer">
    <div class="footer-contact">
      <div>For further information please call or email <span class="hl">Mara Delorme</span></div>
      <div class="row"><svg viewBox="0 0 10 10" aria-hidden="true"><circle cx="5" cy="5" r="5" fill="#29a9e1"/><path d="M3.2 2.6c.3-.2.6 0 .7.3l.3.7c.1.2 0 .4-.2.5l-.3.2c.3.7.8 1.2 1.5 1.5l.2-.3c.1-.2.3-.3.5-.2l.7.3c.3.1.5.4.3.7-.3.6-.9.8-1.5.6C4.1 6.6 3.4 5.9 3 4.6c-.2-.7 0-1.5.2-2z" fill="#fff"/></svg>250.555.0148</div>
      <div class="row"><svg viewBox="0 0 10 10" aria-hidden="true"><circle cx="5" cy="5" r="5" fill="#29a9e1"/><rect x="2.6" y="3.3" width="4.8" height="3.4" fill="none" stroke="#fff" stroke-width=".8"/><path d="M2.6 3.4 5 5.3l2.4-1.9" fill="none" stroke="#fff" stroke-width=".8"/></svg>events@tallowcreekfn.com</div>
    </div>
    <div class="footer-web">TALLOWCREEKFN.COM</div>
  </footer>
</section>

<!-- Page 2: dates and schedule -->
<section class="page dates">
  <div class="photo action-photo" role="img" aria-label="Photo of a saddle bronc rider on a paint horse in the rodeo arena"></div>
  <div class="abs date-panel"></div>
  <h2 class="date-head">Rodeo Date</h2>
  <div class="day-box" style="left:313px;top:68px">28</div>
  <div class="day-box" style="left:392px;top:68px">29</div>
  <div class="day-box" style="left:353px;top:146px">30</div>
  <div class="date-month">July 2023</div>
  <div class="abs intro-band">Saddle up for the Tallow Creek Stampede held at the Tallow Creek First Nation Rodeo grounds!<br>This is now a 3 day family fun event  with the addition of a Friday afternoon Gymkhana!<br>Tallow Creek Stampede has been running for over 30 years and we are exciting to bring the excitement back.</div>

  <div class="sched-day" style="top:354px">28</div>
  <div class="sched-note" style="top:381px">Gymkhana and family Dance</div>
  <div class="sched-rule" style="top:403px"></div>

  <div class="sched-day" style="top:419px">29</div>
  <div class="slot junior" style="top:413px"><span>JUNIOR RODEO</span><span>AT 11 AM</span></div>
  <div class="slot main" style="top:437px"><span>MAIN RODEO STARTS &nbsp; AT 2PM</span></div>
  <div class="sched-note" style="top:467px">with Steak Dinner and Rodeo dance to follow  Band is The Dry Creek Ramblers</div>
  <div class="sched-rule" style="top:488px"></div>

  <div class="sched-day" style="top:503px">30</div>
  <div class="slot junior" style="top:499px"><span>JUNIOR RODEO</span><span>AT 11 AM</span></div>
  <div class="slot main" style="top:523px"><span>MAIN RODEO STARTS &nbsp; AT 2PM</span></div>
  <div class="sched-note" style="top:553px">Free Pancake Breakfast both Saturday and Sunday Morning<br>Cultural Events happening throughout the day.</div>

  <footer class="abs dates-footer">
    <div><span class="label">INFORMATION :</span> Dance – July 29 The Dry Creek Ramblers Picture provided</div>
    <div class="label" style="margin-top:6px">SHARE YOU COMPANIES VALUE:</div>
    <div>Have a look and let us know how we can help you connect with the Right network for you.</div>
  </footer>
</section>

<!-- Page 3: package comparison -->
<section class="page packages">
  <div class="brand"><span class="brand-dot"></span><span class="brand-name">Tallow Creek First Nation</span></div>
  <h2 class="abs pack-banner">Rodeo Packages</h2>
  <table class="pack-table">
    <colgroup><col class="label"><col span="9"></colgroup>
    <thead>
      <tr><th></th><th>Starter<br>Package</th><th>Bronze<br>Package</th><th>Silver<br>Package</th><th>Gold<br>Package</th><th>Platinum<br>Package</th><th>Saloon<br>Package</th><th>Pancake<br>Breakfast<br>Package</th><th>Kids Fun<br>Package</th><th>Steak<br>Dinner</th></tr>
    </thead>
    <tbody>
      <tr class="row-radio" style="height:63px"><th style="vertical-align:bottom;padding-bottom:6px">Pre event<br>radio advertising</th><td></td><td></td><td></td><td></td><td><svg class="tick"><use href="#tick"/></svg></td><td><svg class="tick"><use href="#tick"/></svg></td><td style="vertical-align:top;padding-top:6px"><span class="note">2 MORNINGS</span></td><td></td><td><svg class="tick"><use href="#tick"/></svg></td></tr>
      <tr style="height:38px"><th>Company logo<br>on posters</th><td></td><td></td><td></td><td></td><td><svg class="tick"><use href="#tick"/></svg></td><td><svg class="tick"><use href="#tick"/></svg></td><td></td><td></td><td><svg class="tick"><use href="#tick"/></svg></td></tr>
      <tr style="height:38px"><th>Social media ads<br>and mentions</th><td></td><td><svg class="tick"><use href="#tick"/></svg></td><td><svg class="tick"><use href="#tick"/></svg></td><td><svg class="tick"><use href="#tick"/></svg></td><td><svg class="tick"><use href="#tick"/></svg></td><td><svg class="tick"><use href="#tick"/></svg></td><td><svg class="tick"><use href="#tick"/></svg></td><td><svg class="tick"><use href="#tick"/></svg></td><td><svg class="tick"><use href="#tick"/></svg></td></tr>
      <tr style="height:39px"><th>Company logo<br>on big screen</th><td><svg class="tick"><use href="#tick"/></svg></td><td><svg class="tick"><use href="#tick"/></svg></td><td><svg class="tick"><use href="#tick"/></svg></td><td><svg class="tick"><use href="#tick"/></svg></td><td><svg class="tick"><use href="#tick"/></svg></td><td><svg class="tick"><use href="#tick"/></svg></td><td><svg class="tick"><use href="#tick"/></svg></td><td><svg class="tick"><use href="#tick"/></svg></td><td><svg class="tick"><use href="#tick"/></svg></td></tr>
      <tr style="height:38px"><th>Company logo<br>on web &amp; program</th><td><svg class="tick"><use href="#tick"/></svg></td><td><svg class="tick"><use href="#tick"/></svg></td><td><svg class="tick"><use href="#tick"/></svg></td><td><svg class="tick"><use href="#tick"/></svg></td><td><svg class="tick"><use href="#tick"/></svg></td><td><svg class="tick"><use href="#tick"/></svg></td><td><svg class="tick"><use href="#tick"/></svg></td><td><svg class="tick"><use href="#tick"/></svg></td><td><svg class="tick"><use href="#tick"/></svg></td></tr>
      <tr style="height:39px"><th>Commercial on<br>the big screen</th><td></td><td></td><td></td><td></td><td><svg class="tick"><use href="#tick"/></svg></td><td><svg class="tick"><use href="#tick"/></svg></td><td></td><td></td><td><svg class="tick"><use href="#tick"/></svg></td></tr>
      <tr style="height:50px"><th>Large banners<br>(sponsor provided)<br>in arena</th><td></td><td></td><td><svg class="tick"><use href="#tick"/></svg></td><td><svg class="tick"><use href="#tick"/></svg></td><td><svg class="tick"><use href="#tick"/></svg><span class="qty">(2)</span></td><td><svg class="tick"><use href="#tick"/></svg><span class="qty">(2)</span></td><td></td><td></td><td><svg class="tick"><use href="#tick"/></svg><span class="qty">(2)</span></td></tr>
      <tr style="height:31px"><th>Weekend passes</th><td></td><td></td><td><svg class="tick"><use href="#tick"/></svg><span class="qty">(4)</span></td><td><svg class="tick"><use href="#tick"/></svg><span class="qty">(6)</span></td><td><svg class="tick"><use href="#tick"/></svg><span class="qty">(8)</span></td><td><svg class="tick"><use href="#tick"/></svg><span class="qty">(6)</span></td><td><svg class="tick"><use href="#tick"/></svg><span class="qty">(4)</span></td><td><svg class="tick"><use href="#tick"/></svg><span class="qty">(2)</span></td><td><svg class="tick"><use href="#tick"/></svg><span class="qty">(6)</span></td></tr>
      <tr style="height:60px"><th>Dance tickets<br>(must be age of<br>majority) including<br>steak dinner</th><td></td><td></td><td></td><td><svg class="tick"><use href="#tick"/></svg><span class="qty">(6)</span></td><td><svg class="tick"><use href="#tick"/></svg><span class="qty">(8)</span></td><td><svg class="tick"><use href="#tick"/></svg><span class="qty">(6)</span></td><td></td><td></td><td><svg class="tick"><use href="#tick"/></svg><span class="qty">(6)</span></td></tr>
      <tr style="height:51px"><th style="vertical-align:top;padding-top:8px">Admission tickets<br>to Sunday rodeo</th><td style="vertical-align:top;padding-top:10px"><svg class="tick"><use href="#tick"/></svg><span class="qty">(2)</span></td><td style="vertical-align:top;padding-top:10px"><svg class="tick"><use href="#tick"/></svg><span class="qty">(4)</span></td><td></td><td></td><td></td><td></td><td></td><td></td><td></td></tr>
    </tbody>
  </table>
</section>

<!-- Page 4: invoice -->
<section class="page invoice">
  <div class="abs inv-title">INVOICE</div>
  <div class="abs inv-cust-bar">CUSTOMER INFORMATION</div>
  <div class="abs inv-cust">
    <b>Company name:</b><span>Lorem Ipsum</span>
    <b>Attention:</b><span>Lorem Ipsum</span>
    <b>Address:</b><span>Lorem Ipsum</span>
    <b>Phone number:</b><span>Lorem Ipsum</span>
    <b>Date:</b><span>Lorem Ipsum</span>
  </div>
  <div class="brand"><span class="brand-dot"></span><span class="brand-name">Tallow Creek First Nation</span></div>

  <div class="sec-bar" style="top:192px">RODEO PACKAGES</div>
  <div class="sec-head" style="top:205px"><span style="left:194px">QTY</span><span style="left:268px">COST</span><span style="left:391px">TOTAL</span></div>
  <div class="item-list" style="top:228px">Starter Package<br>Bronze Package<br>Silve Package<br>Gold Package<br>Platinum Package</div>
  <div class="vline" style="left:191px;top:222px;height:102px"></div>
  <div class="vline" style="left:265px;top:222px;height:102px"></div>
  <div class="vline" style="left:338px;top:222px;height:102px"></div>
  <div class="sum-bar" style="left:337px;top:332px"></div>

  <div class="sec-bar" style="top:364px">EVENT PACKAGES</div>
  <div class="sec-head" style="top:377px"><span style="left:188px">QTY</span><span style="left:262px">COST</span><span style="left:385px">TOTAL</span></div>
  <div class="item-list" style="top:398px">Saloon Package<br>Pancake Breakfast Package<br>Kid’s Fun Package<br>Steak Dinner Pakage</div>
  <div class="vline" style="left:193px;top:393px;height:101px"></div>
  <div class="vline" style="left:267px;top:393px;height:101px"></div>
  <div class="vline" style="left:340px;top:393px;height:101px"></div>
  <div class="sum-bar" style="left:339px;top:504px"></div>

  <div class="abs total-label">TOTAL INVOICE</div>
  <div class="abs total-box"></div>
  <div class="abs paid"><b>Paid By Cheque:</b>Lorem Ipsum</div>

  <footer class="abs inv-footer"><span style="left:44px">Address</span><span style="left:238px">Phone</span><span style="left:433px">Email</span></footer>
  <div class="abs inv-name">TALLOW CREEK FIRST NATION</div>
</section>

</body>
</html>
```